Poster Design Project

We are a non-profit organization that organizes various social events for Indian senior citizens to promote a healthy lifestyle, share knowledge & companionship among them.

One such event that we are organizing for them is, "Lanterns and Footwork Gala" - (On the lines of Steps Under Lanterns), with the seniors as our stars.

We need a poster design for this event that incorporates the Steps Under Lanterns theme as well as some Indian Cinema (Bollywood) themes. We are open to different color schemes and design concepts.

The poster design should include the event location, time, ticket prices, contact information (up to 3 contacts), and a small note (i.e. "Snacks will be available for purchase."). We are also looking for a flyer design which would be similar to the poster.

We have uploaded our organization logo for your reference.

Indian Community (Families and Senior Citizens)

Non-Profit

• Focused on seniors as our stars
Should look professional
• It would be great if an event based logo could be put on the poster and flyer, which would be based on/integrated with the organization logo. The concept used in files 2 and 9 could be combined with the organization logo (file 6) to form the event logo.

Some ideas we thought of were movie posters, "Steps Under Lanterns", "Kadam Milao Re" or similar shows' concepts, etc.

We have attached some more images as examples of some indian dance movie posters.
• It's a family event so

```html
<!DOCTYPE html>
<html lang="en">
<head>
<meta charset="utf-8">
<title>Lanterns and Footwork Gala — Poster</title>
<link rel="stylesheet" href="https://fonts.googleapis.com/css2?family=Arimo:wght@700&family=Comfortaa:wght@500;700&family=Questrial&family=Yellowtail&family=Lexend:ital,wght@0,800&display=swap">
<style>
  :root{
    --sky-light:#3fb4ec;
    --sky-mid:#1768b4;
    --sky-deep:#071f55;
    --mist:#c6d3e6;
    --ring:#d9f1ff;
    --neon-red:#ff3b2c;
    --neon-glow:#ffb25e;
    --neon-green:#8dff3a;
    --banner:#fff200;
    --venue-label:#e8141c;
    --venue-name:#1b1bf0;
    --timing:#e8141c;
    --contact:#7e24a6;
    --brand:#f05a22;
    --white:#ffffff;
    --ink:#111111;
  }
  *{margin:0;padding:0;box-sizing:border-box}
  html,body{width:750px;height:1200px;overflow:hidden;background:var(--sky-deep)}
  .poster{
    position:relative;width:750px;height:1200px;overflow:hidden;
    background:
      radial-gradient(ellipse 520px 460px at 330px 210px, var(--sky-light) 0%, var(--sky-mid) 45%, transparent 80%),
      linear-gradient(180deg, var(--sky-deep) 0%, #0c3a86 35%, #3f79c0 65%, var(--mist) 100%);
    font-family:'Arimo',Arial,sans-serif;
  }
  .ring{position:absolute;left:0;top:0}
  .brand{
    position:absolute;left:50px;top:40px;width:168px;height:116px;
    background:var(--brand);display:flex;align-items:center;justify-content:center;
    font-family:'Questrial',sans-serif;font-size:40px;color:var(--white);
  }
  .title{position:absolute;left:0;top:0;width:750px;height:470px}
  .title__lead{
    position:absolute;left:52px;top:185px;transform:rotate(-9deg);transform-origin:left bottom;
    font-family:'Comfortaa',sans-serif;font-weight:700;font-size:82px;color:#ffe9d6;
    -webkit-text-stroke:3px var(--neon-red);
    text-shadow:0 0 6px var(--neon-red),0 0 16px var(--neon-glow);
    letter-spacing:1px;
  }
  .title__link{
    position:absolute;left:300px;top:250px;transform:rotate(-12deg);
    font-family:'Yellowtail',cursive;font-size:56px;color:#d8ff9c;
    text-shadow:0 0 6px var(--neon-green),0 0 14px var(--neon-green);
  }
  .title__main{
    position:absolute;left:200px;top:322px;transform:rotate(-10deg);
    font-family:'Lexend',sans-serif;font-weight:800;font-style:italic;font-size:104px;
    color:var(--white);letter-spacing:6px;
    text-shadow:0 4px 0 #8fb6dc,0 0 18px rgba(255,255,255,.5);
  }
  .star{position:absolute;left:92px;top:310px}
  .photo{
    position:absolute;left:-40px;top:488px;width:510px;height:555px;border-radius:50%;
    background:radial-gradient(ellipse at 55% 45%, #cfe6ff 0%, #4a8fd6 30%, #113c86 65%, #061c4e 100%);
  }
  .venue{
    position:absolute;left:458px;top:630px;width:292px;height:56px;background:var(--banner);
    display:flex;align-items:center;justify-content:center;gap:6px;letter-spacing:-1px;
  }
  .venue__label{color:var(--venue-label);font-size:19px}
  .venue__name{color:var(--venue-name);font-size:27px}
  .tickets{
    position:absolute;left:482px;top:770px;width:204px;height:204px;border-radius:50%;
    background:radial-gradient(circle at 45% 30%, #2a8fde 0%, #0b4aa0 55%, #062a6c 100%);
    box-shadow:0 0 0 3px rgba(255,255,255,.35);
    text-align:center;color:var(--white);
  }
  .tickets__label{font-family:'Questrial',sans-serif;font-size:19px;line-height:20px;margin-top:28px}
  .tickets__price{font-family:'Comfortaa',sans-serif;font-weight:700;color:var(--banner);font-size:42px;line-height:44px}
  .tickets__to{font-family:'Comfortaa',sans-serif;font-weight:700;color:var(--banner);font-size:24px;line-height:22px}
  .tickets__price--high{font-size:36px;line-height:40px}
  .timings{
    position:absolute;left:0;top:1042px;width:292px;height:54px;background:var(--banner);
    display:flex;align-items:center;padding-left:10px;
    color:var(--timing);font-size:25px;letter-spacing:-1px;
  }
  .note{
    position:absolute;left:0;top:1128px;width:388px;height:54px;background:var(--banner);
    display:flex;align-items:center;padding-left:12px;
    font-family:'Questrial',sans-serif;font-size:21px;color:var(--ink);
  }
  .contacts{
    position:absolute;left:438px;top:1020px;list-style:none;
    color:var(--contact);font-size:20px;line-height:27px;letter-spacing:-1px;
  }
</style>
</head>
<body>
<main class="poster">
  <svg class="ring" width="750" height="1200" viewBox="0 0 750 1200" aria-hidden="true">
    <circle cx="378" cy="300" r="250" fill="none" stroke="var(--ring)" stroke-width="7"
            stroke-dasharray="560 90 420 500" stroke-dashoffset="-120" stroke-linecap="round"
            style="filter:drop-shadow(0 0 6px #9fdcff)"/>
  </svg>

  <div class="brand">Saathi</div>

  <h1 class="title">
    <span class="title__lead">Lanterns</span>
    <span class="title__link">and footwork</span>
    <span class="title__main">GALA</span>
  </h1>

  <svg class="star" width="92" height="92" viewBox="0 0 100 100" aria-hidden="true">
    <polygon points="50,6 62,38 96,38 68,58 79,92 50,71 21,92 32,58 4,38 38,38"
             fill="none" stroke="var(--neon-green)" stroke-width="5" stroke-linejoin="round"
             style="filter:drop-shadow(0 0 6px var(--neon-green))"/>
  </svg>

  <div class="photo" role="img" aria-label="Photograph of a dancing couple in white costumes performing a dip on a blue-lit stage"></div>

  <div class="venue"><span class="venue__label">Venue:</span><span class="venue__name">Dance Centre</span></div>

  <div class="tickets">
    <p class="tickets__label">Tickets<br>Availble</p>
    <p class="tickets__price">₹.500/-</p>
    <p class="tickets__to">to</p>
    <p class="tickets__price tickets__price--high">₹.1000/-</p>
  </div>

  <div class="timings">Timings: 7 to midnight</div>
  <div class="note">Snacks will be available for purchase.</div>

  <ul class="contacts">
    <li>Contact at: Ph. 011 4567 2390</li>
    <li>www.saathi.org.in</li>
    <li>Contact at: Ph. 011 4567 2390</li>
    <li>www.saathi.org.in</li>
    <li>Contact at: Ph. 011 4567 2390</li>
    <li>www.saathi.org.in</li>
  </ul>
</main>
</body>
</html>
```